Copper Ridge Garage Door Sales & Repair needs a Business Card Design

I need a business card design to go with our new business logo that was created a few months ago.

Copper Ridge Garage Door specializes in selling and installing new garage doors, and new garage door openers. We also take care of all repairs to existing garage doors and garage door openers. All makes and models.

Target Market(s)

Home-owners, renters, anyone who lives in a house and has a garage. Residential and commercial garages.

Industry/Entity Type

Home Improvement

Contact Information for Business Card

I would like the business cards to have rounded corners and be double-sided. My old logo is still on my website at www.copperridgegarage.example. If I was going to incorporate a secondary color on the business cards, I think that orange is a good choice (especially since blue and orange are the colors of our Tulsa Kestrels), but I'm not opposed to seeing a different color if another color works better with my logo colors. I have two logo colors. One designed for a white background and one designed for a darker background. I'm not opposed to using both. Maybe a dark background with the white logo on one side, and a white background with the other logo color on the other side.

My business is a small, locally owned business that I am trying to grow. But I would like my business cards to look very professional. Like we have been in business for a long time. I like traditional to modern looking cards. Just something bold and memorable. My full company name is Copper Ridge Garage Door Sales & Repair. But you can just do COPPER RIDGE GARAGE DOOR, if that works better.

Font styles to use
Serif
Script

Requirements
Must have
• Rounded corners
• Double-sided
• 3-D Elements. Layering of some sort (a sketch of a garage door or a 3rd color (orange) brought in some how. I really like watermarks.
• Matte cards that you can write on.
• White on one side. (Or the lighter blue in my logo). Darker blue logo color on the other side.
• I would like our tag line on the cards somewhere... "For All Your Garage Door Needs".
• I would also like "Call For a FREE Estimate" by the phone number.
• And "Serving the Greater Metro Denver Area" somewhere on the card as well.
Nice to have
• Refer to "Business Card Details" above.

```html
<!DOCTYPE html>
<html lang="en">
<head>
<meta charset="utf-8">
<title>Copper Ridge Garage Door — Business Card</title>
<link rel="stylesheet" href="https://fonts.googleapis.com/css2?family=Open+Sans:wght@400;600;700&display=swap">
<style>
  :root {
    --page: #eceef1;
    --navy: #425071;
    --sky: #b3c6d4;
    --sky-light: #c2d2de;
    --sky-soft: #c7d5e2;
    --white: #ffffff;
  }
  * { margin: 0; padding: 0; box-sizing: border-box; }
  html, body { width: 1200px; height: 900px; overflow: hidden; }
  body {
    background: var(--page);
    font-family: "Open Sans", Arial, sans-serif;
    position: relative;
  }
  .card {
    position: absolute;
    background: var(--navy);
    border-radius: 14px;
    overflow: hidden;
    box-shadow: 0 6px 18px rgba(30, 40, 60, 0.18);
  }
  .card-front { left: 238px; top: 62px; width: 555px; height: 343px; }
  .card-back  { left: 458px; top: 519px; width: 558px; height: 343px; }

  .contact-list {
    position: absolute; left: 20px; top: 49px; z-index: 2;
    list-style: none; color: var(--white);
    font-size: 14.5px; line-height: 20px;
  }
  .person {
    position: absolute; right: 31px; top: 53px; text-align: right; z-index: 2;
  }
  .person-name { color: var(--sky-soft); font-size: 20px; font-weight: 600; line-height: 26px; }
  .person-role { color: var(--white); font-size: 14.5px; line-height: 20px; }

  .ridge-art {
    position: absolute; left: -30px; right: -30px; top: 122px; height: 300px;
    border-radius: 50% 50% 0 0 / 260px 260px 0 0;
    background: linear-gradient(to bottom, var(--sky-light) 0%, var(--sky) 45%, var(--sky) 100%);
  }
  .estimate-line {
    position: absolute; left: 0; right: 0; bottom: 18px; z-index: 2;
    text-align: center; color: var(--navy); font-size: 16.5px;
  }
  .estimate-line .divider { margin: 0 6px; }

  .brand {
    position: absolute; left: 0; right: 0; top: 70px;
    display: flex; flex-direction: column; align-items: center; gap: 14px;
  }
  .brand-dot { width: 34px; height: 34px; border-radius: 50%; background: var(--sky); }
  .brand-name {
    color: var(--white); font-weight: 700; font-size: 27px;
    letter-spacing: 1px; text-align: center; line-height: 33px;
  }
  .service-lines {
    position: absolute; left: 0; right: 0; top: 249px;
    text-align: center; color: var(--white);
    font-weight: 600; font-size: 14.5px; line-height: 30px;
    text-transform: uppercase;
  }
</style>
</head>
<body>
  <section class="card card-front">
    <div class="ridge-art" role="img" aria-label="Pale blue mountain silhouette with a garage set into the slope"></div>
    <ul class="contact-list">
      <li>T: 044-555 010 789</li>
      <li>E: info@copperridgegarage.example</li>
      <li>w: www.copperridgegarage.example</li>
    </ul>
    <div class="person">
      <p class="person-name">Daniel Harper</p>
      <p class="person-role">Managing Director</p>
    </div>
    <p class="estimate-line">Call For a FREE Estimate<span class="divider">|</span>044 555 0147</p>
  </section>

  <section class="card card-back">
    <div class="brand">
      <span class="brand-dot"></span>
      <p class="brand-name">COPPER RIDGE<br>GARAGE DOOR</p>
    </div>
    <p class="service-lines">Serving the Greater Metro Denver Area<br>For All Your Garage Door Needs</p>
  </section>
</body>
</html>
```